Business Card Design Project

A double sided business card for presentation to business leaders in corporate.

Target Market(s)

Corporate, business professionals, HR

Industry/Entity Type

Business

Requirements
Must have
• FRONT

Logo

www.brightfernco.com.au

BACK

Maren Tollvey-Hart
Director

+ 61 (0) 418 556 230
maren@brightfernco.com.au
www.brightfernco.com.au

Results through energy and team engagement

("ripples" of logo, bottom corner)

Must be:
- double sided
size: 86 x 54mm
supplied as one pdf with crop marks shown (+- 1mm, with 2-3 mm bleed)

```html
<!DOCTYPE html>
<html lang="en">
<head>
<meta charset="utf-8">
<title>Bright Fern Co Business Cards</title>
<link href="https://fonts.googleapis.com/css2?family=Ubuntu:wght@300;400;500;700&display=swap" rel="stylesheet">
<style>
  :root {
    --page-bg: #e4e4e6;
    --silver-light: #fbfbfb;
    --silver-mid: #e6e6e8;
    --silver-dark: #cfcfd2;
    --band-dark: #4a4a4e;
    --band-light: #7a7a7e;
    --plum-deep: #24071d;
    --plum-mid: #3f1035;
    --plum-soft: #6a2a5c;
    --accent-purple: #8a2f7b;
    --ink-grey: #555558;
    --text-white: #ffffff;
  }
  * { box-sizing: border-box; margin: 0; padding: 0; }
  html, body {
    width: 1200px;
    height: 861px;
    overflow: hidden;
  }
  body {
    background: var(--page-bg);
    font-family: "Ubuntu", sans-serif;
    position: relative;
  }
  .card {
    position: absolute;
    top: 268px;
    width: 520px;
    height: 326px;
    border-radius: 16px;
    overflow: hidden;
    box-shadow: 0 10px 28px rgba(0,0,0,0.18);
    background: linear-gradient(180deg, var(--silver-light) 0%, var(--silver-mid) 60%, var(--silver-dark) 100%);
  }
  .card--front { left: 50px; }
  .card--back { left: 630px; }

  .card__band {
    position: absolute;
    left: 0; right: 0;
    background: linear-gradient(180deg, var(--band-light) 0%, var(--band-dark) 100%);
  }
  .card__plum {
    position: absolute;
    left: 0; right: 0; bottom: 0;
    background: linear-gradient(160deg, var(--plum-deep) 0%, var(--plum-mid) 55%, var(--plum-soft) 100%);
  }

  /* Front */
  .card--front .card__band { top: 182px; height: 32px; }
  .card--front .card__plum { top: 214px; }
  .brand-mark {
    position: absolute;
    top: 70px;
    left: 0; right: 0;
    display: flex;
    align-items: center;
    justify-content: center;
    gap: 14px;
  }
  .brand-mark__dot {
    width: 18px; height: 18px;
    border-radius: 50%;
    background: var(--accent-purple);
  }
  .brand-mark__name {
    font-size: 44px;
    font-weight: 400;
    color: var(--ink-grey);
    letter-spacing: -0.5px;
  }
  .front-tagline {
    position: absolute;
    left: 0; right: 0;
    top: 236px;
    text-align: center;
    color: var(--text-white);
    font-size: 23px;
    font-weight: 500;
    line-height: 1.36;
  }

  /* Back */
  .card--back .card__band { top: 150px; height: 36px; }
  .card--back .card__plum { top: 186px; }
  .back-brand {
    position: absolute;
    top: 68px;
    left: 38px;
    display: flex;
    align-items: center;
    gap: 10px;
  }
  .back-brand__dot {
    width: 14px; height: 14px;
    border-radius: 50%;
    background: var(--accent-purple);
  }
  .back-brand__name {
    font-size: 28px;
    font-weight: 400;
    color: var(--ink-grey);
    letter-spacing: -0.4px;
  }
  .holder {
    position: absolute;
    top: 62px;
    right: 22px;
    text-align: left;
  }
  .holder__name {
    font-size: 25px;
    font-weight: 700;
    color: var(--accent-purple);
  }
  .holder__role {
    font-size: 16px;
    font-weight: 700;
    color: var(--ink-grey);
    margin-top: 2px;
  }
  .back-tagline {
    position: absolute;
    top: 150px;
    left: 58px;
    height: 36px;
    line-height: 36px;
    font-size: 17px;
    font-weight: 300;
    color: var(--text-white);
    letter-spacing: 0.2px;
  }
  .contact {
    position: absolute;
    top: 214px;
    left: 58px;
    list-style: none;
    color: var(--text-white);
    font-size: 18px;
    font-weight: 400;
  }
  .contact__item { line-height: 32px; }
  .contact__label { font-weight: 700; }
</style>
</head>
<body>
  <section class="card card--front" aria-label="Business card front">
    <div class="brand-mark">
      <span class="brand-mark__dot"></span>
      <span class="brand-mark__name">Bright Fern Co</span>
    </div>
    <div class="card__band"></div>
    <div class="card__plum"></div>
    <p class="front-tagline">Results through energy and<br>team engagement</p>
  </section>

  <section class="card card--back" aria-label="Business card back">
    <div class="back-brand">
      <span class="back-brand__dot"></span>
      <span class="back-brand__name">Bright Fern Co</span>
    </div>
    <div class="holder">
      <p class="holder__name">Maren Tollvey-Hart</p>
      <p class="holder__role">Director</p>
    </div>
    <div class="card__band"></div>
    <p class="back-tagline">Results through energy and team engagement</p>
    <div class="card__plum"></div>
    <ul class="contact">
      <li class="contact__item"><span class="contact__label">Phone:</span> + 61 (0) 418 556 230</li>
      <li class="contact__item"><span class="contact__label">E-mail:</span> maren@brightfernco.com.au</li>
      <li class="contact__item"><span class="contact__label">Website:</span> www.brightfernco.com.au</li>
    </ul>
  </section>
</body>
</html>
```